Flyer YOga studio

I need a double sided DL flyer (landscape) with my yoga studio details on one side and my timetable on the back.

It looks like a lot of my info didn't save the orignal brief.

here is some information.

On the front side - Logo to be centred on white background.

Underneath text
$20 for 7 days unlimited yoga/pilates/run group
$99 for 1 month unlimited

also to be included - Location: Upstairs, 17 North Parade Linwood 3218
0438 915602
info@havenlinwood.com.au
www.havenlinwood.com.au

ON back side - Timetable only

Landscape

• Following text should be on front side

the logo
New clients offer: $20 for 7 days of Yoga
$99 - 1 month unlimited

Location: Upstairs, 17 North Parade
Linwood VIC 3218
info@havenlinwood.com.au/0438 915602

The following text:
Stretch...strength...Run
Any order you like...pick all or one. Only fear holds you back from experiencing any of these. We teach all our classes to what is happening in your body in this moment with an eye for alignment, correct muscle recruitment and breath awareness.

On the back:
Class descriptions:
Yoga: Flowing Vinyasa classes that heat the body through dynamic movements and slowing down for deep hip openers and relaxation.
Pilates: Mat classes for healthy bodies using a systematic sequencing of exercises that works the whole body, developing strength, flexibility and mindfulness.
Run groups: A non competitive session where you set the goals and we help you meet them, whether it getting to the corner and back or your first marathon.

```html
<!DOCTYPE html>
<html lang="en">
<head>
<meta charset="utf-8">
<title>Halden Studio – DL Flyer</title>
<link href="https://fonts.googleapis.com/css2?family=Arimo:wght@400;700&display=swap" rel="stylesheet">
<style>
  :root {
    --page: #ebe6de;
    --card-top: #f8f6f2;
    --card-mid: #efe9df;
    --ink: #5b5b5b;
    --ink-soft: #808080;
    --rule: #9a9a9a;
    --grid: #cbc4b8;
    --red: #e3262a;
    --flow: #fdc116;
    --flow-short: #f7e81c;
    --run: #b7dde9;
    --pilates: #95c95c;
    --express: #b7a6d3;
    --kids: #d74ea3;
  }
  * { box-sizing: border-box; margin: 0; padding: 0; }
  html, body { width: 1200px; height: 1132px; overflow: hidden; }
  body {
    background: var(--page);
    font-family: "Arimo", Arial, sans-serif;
    color: var(--ink);
    position: relative;
  }
  .card {
    position: absolute;
    left: 150px;
    width: 904px;
    height: 426px;
    overflow: hidden;
    background: linear-gradient(180deg, var(--card-top) 0%, var(--card-mid) 100%);
    box-shadow: 0 3px 8px rgba(0,0,0,.25);
  }
  .card--front { top: 104px; }
  .card--back { top: 611px; }

  .front__band { position: absolute; inset: 0; width: 100%; height: 100%; }

  .intro {
    position: absolute; left: 22px; top: 20px;
    font-size: 15px; line-height: 22px; color: var(--ink-soft);
    white-space: nowrap;
  }

  .brand {
    position: absolute; left: 170px; top: 228px; width: 420px;
    text-align: center;
    font-size: 38px; font-weight: 400; color: var(--ink);
    letter-spacing: .5px;
  }

  .offer { position: absolute; left: 661px; top: 16px; width: 224px; }
  .offer__ornament {
    display: block; margin: 0 auto; width: 140px; height: 36px;
    background: linear-gradient(180deg, #ece3d4, #d7c7ab);
    border-radius: 18px 18px 0 0;
  }
  .offer__rule { height: 1px; background: var(--rule); margin-top: 3px; }
  .offer__title {
    text-align: center; font-weight: 700; font-size: 15px;
    margin-top: 10px; color: var(--ink);
  }
  .offer__table {
    margin-top: 9px; width: 224px; height: 167px;
    border: 1.5px dashed var(--rule); border-radius: 12px;
    display: grid; grid-template-rows: 104px 1fr;
    grid-template-columns: 66px 1fr;
  }
  .offer__price {
    display: flex; align-items: center; justify-content: center;
    font-size: 22px; font-weight: 700; color: var(--ink);
    border-right: 1px solid var(--rule);
  }
  .offer__desc {
    display: flex; align-items: center; justify-content: center;
    text-align: center; font-size: 15px; line-height: 19px; padding: 0 6px;
    color: var(--ink);
  }
  .offer__table > :nth-child(-n+2) { border-bottom: 1px solid var(--rule); }

  .contact { position: absolute; left: 22px; top: 346px; font-size: 17px; line-height: 21px; color: var(--ink); }
  .contact__label { font-weight: 700; font-size: 18px; }

  .phone {
    position: absolute; right: 20px; top: 302px; text-align: right;
    color: var(--red); font-weight: 700; font-size: 28px; line-height: 35px;
  }
  .web {
    position: absolute; right: 20px; top: 384px;
    font-weight: 700; font-size: 23px; color: var(--ink);
  }

  .timetable {
    position: absolute; left: 21px; top: 20px;
    width: 862px; height: 386px;
    border: 1.5px dashed var(--rule); border-radius: 14px;
    overflow: hidden;
  }
  .timetable table {
    width: 100%; height: 100%;
    border-collapse: collapse; table-layout: fixed;
    font-size: 15px; text-align: center; color: #333;
  }
  .timetable col.time { width: 88px; }
  .timetable th, .timetable td {
    border: 1px solid var(--grid); line-height: 16px; padding: 0 2px;
    height: 38px; overflow: hidden;
  }
  .timetable tr.days > * { height: 42px; font-size: 16.5px; color: var(--ink); }
  .timetable tr:first-child > * { border-top: none; }
  .timetable tr > :first-child { border-left: none; }
  .timetable tr > :last-child { border-right: none; }
  .timetable tr:last-child > * { border-bottom: none; }
  .timetable th.slot { font-weight: 700; font-size: 16px; color: var(--ink); }

  .c-flow { background: var(--flow); }
  .c-flow-short { background: var(--flow-short); }
  .c-run { background: var(--run); }
  .c-pilates { background: var(--pilates); }
  .c-express { background: var(--express); }
  .c-kids { background: var(--kids); }
</style>
</head>
<body>

<section class="card card--front">
  <svg class="front__band" viewBox="0 0 904 426" preserveAspectRatio="none" aria-hidden="true">
    <defs>
      <linearGradient id="tanFade" x1="0" y1="0" x2="0" y2="1">
        <stop offset="0" stop-color="#f1ebe1"/>
        <stop offset="0.55" stop-color="#e4d6bf"/>
        <stop offset="1" stop-color="#c6a778"/>
      </linearGradient>
    </defs>
    <path d="M0 262 C 250 222, 600 214, 904 256 L904 426 L0 426 Z" fill="url(#tanFade)"/>
  </svg>

  <p class="intro">Stretch...strength...Run<br>Any order you like...pick all or<br>one. Only fear holds you back<br>from experiencing any of these.<br>We teach all our classes to what<br>is happening in your body in this<br>moment with an eye for alignment,<br>correct muscle recruitment and<br>breath awareness.</p>

  <div class="brand">Halden Studio</div>

  <div class="offer">
    <span class="offer__ornament" role="img" aria-label="Decorative flourish ornament"></span>
    <div class="offer__rule"></div>
    <div class="offer__title">NEW CLIENTS OFFER</div>
    <div class="offer__table">
      <div class="offer__price">$20</div>
      <div class="offer__desc">7 days of classes<br>unlimited (yoga,<br>pilates<br>and run group)</div>
      <div class="offer__price">$99</div>
      <div class="offer__desc">1 month<br>unlimited</div>
    </div>
  </div>

  <div class="contact">
    <div class="contact__label">LOCATION:</div>
    <div>Upstairs, 17 North Parade, Linwood, 3218</div>
    <div>info@havenlinwood.com.au</div>
  </div>

  <div class="phone">Phone<br>0438 915602</div>
  <div class="web">www.havenlinwood.com.au</div>
</section>

<section class="card card--back">
  <div class="timetable">
    <table>
      <colgroup><col class="time"><col><col><col><col><col><col><col></colgroup>
      <tr class="days"><th></th><th>Monday</th><th>Tuesday</th><th>Wednesday</th><th>Thursday</th><th>Friday</th><th>Saturday</th><th>Sunday</th></tr>
      <tr><th class="slot">6.15 am</th><td></td><td class="c-flow-short">Flow (60)</td><td></td><td class="c-run">Run group</td><td class="c-flow-short">Flow (60)</td><td></td><td></td></tr>
      <tr><th class="slot">8 am</th><td></td><td></td><td></td><td></td><td></td><td class="c-run">Run group<br>(7 am)</td><td></td></tr>
      <tr><th class="slot">9.30 am</th><td class="c-flow">Flow (75)</td><td class="c-flow">Flow (75)</td><td class="c-flow">Flow (75)</td><td class="c-flow">Flow (75)</td><td class="c-flow">Flow (75)</td><td class="c-flow">Flow (75)</td><td class="c-flow">Flow (75)</td></tr>
      <tr><th class="slot">11 am</th><td></td><td></td><td></td><td></td><td class="c-pilates">Pilates<br>Open (60)</td><td></td><td></td></tr>
      <tr><th class="slot">12.15 pm</th><td class="c-express">Express<br>Pilates</td><td></td><td class="c-express">Express<br>Flow (45)</td><td></td><td class="c-express">Express<br>Flow (45)</td><td></td><td></td></tr>
      <tr><th class="slot">4 pm</th><td class="c-kids">Kids Yoga</td><td></td><td></td><td></td><td></td><td></td><td></td></tr>
      <tr><th class="slot">6 pm</th><td class="c-run">Run group<br>(6.15 pm)</td><td class="c-pilates">Pilates<br>Open (60)</td><td class="c-run">Run group<br>(6.15 pm)</td><td class="c-flow-short">Flow (60)</td><td></td><td></td><td></td></tr>
      <tr><th class="slot">7.15 pm</th><td></td><td class="c-flow">Flow (75)</td><td class="c-flow">Flow (75)</td><td class="c-pilates">Pilates<br>Open (60)</td><td></td><td></td><td></td></tr>
      <tr><th class="slot">7.30 pm</th><td class="c-flow">Flow (75)</td><td></td><td></td><td></td><td></td><td></td><td></td></tr>
    </table>
  </div>
</section>

</body>
</html>
```